Harold Brisk Mechanical business cards

We need business cards designed for "Harold Brisk Mechanical" "Mechanical & Electrical Contractors" "Specializing in Service & Installation"
"Cooling, Heating, Service, Installations, Residential, Commercial"

```html
<!DOCTYPE html>
<html lang="en">
<head>
<meta charset="utf-8">
<title>Harold Brisk Mechanical – Business Cards</title>
<link rel="stylesheet" href="https://fonts.googleapis.com/css2?family=Open+Sans:wght@400;600;700&family=Roboto:wght@400;500&display=swap">
<style>
  :root {
    --backdrop: #7b7b7b;
    --card-light: #eeeeee;
    --card-dark: #000000;
    --brand-red: #e31b23;
    --ink: #111111;
    --ink-soft: #333333;
    --rule: #9a9a9a;
    --white: #ffffff;
  }
  * { margin: 0; padding: 0; box-sizing: border-box; }
  html, body {
    width: 1200px; height: 1200px; overflow: hidden;
    background: var(--backdrop);
  }
  .canvas { position: relative; width: 1200px; height: 1200px; }
  .card {
    position: absolute; top: 310px; width: 364px; height: 594px;
    text-align: center;
  }
  .card--front {
    left: 234px; background: var(--card-light);
    font-family: "Open Sans", sans-serif; color: var(--ink-soft);
  }
  .card--back {
    left: 627px; width: 370px; background: var(--card-dark);
    font-family: "Roboto", sans-serif; color: var(--white);
  }

  /* front */
  .brand-front { position: absolute; top: 92px; left: 0; right: 0; }
  .brand-front__square {
    width: 62px; height: 62px; margin: 0 auto 18px; background: var(--brand-red);
  }
  .brand-front__name {
    font-weight: 700; font-size: 28px; line-height: 34px;
    letter-spacing: 2px; color: var(--ink); text-transform: uppercase;
  }
  .person { position: absolute; top: 340px; left: 0; right: 0; }
  .person__name {
    color: var(--brand-red); font-weight: 600; font-size: 21px; line-height: 28px;
    text-transform: uppercase;
  }
  .person__role { font-size: 17px; line-height: 24px; }
  .rule { width: 206px; height: 1px; background: var(--rule); margin: 0 auto; }
  .person .rule { margin-top: 8px; }
  .contact { list-style: none; margin-top: 8px; font-size: 17px; line-height: 21.5px; }
  .contact__label { color: var(--brand-red); }
  .contact__web { color: var(--ink); font-weight: 600; }
  .contact__web span { color: var(--brand-red); }
  .address { margin-top: 8px; font-size: 17px; line-height: 21.5px; }
  .address-block .rule { margin-top: 8px; }

  /* back */
  .brand-back { position: absolute; top: 150px; left: 0; right: 0; }
  .brand-back__square {
    width: 140px; height: 140px; margin: 0 auto; background: var(--brand-red);
  }
  .brand-back__name {
    margin-top: 18px; font-size: 22px; font-weight: 500;
    letter-spacing: 1px; text-transform: uppercase;
  }
  .tagline {
    position: absolute; top: 365px; left: 0; right: 0;
    font-size: 15px; letter-spacing: 0.2px;
  }
  .services { position: absolute; top: 496px; left: 0; right: 0; font-size: 17px; line-height: 21.5px; }
  .services__title { font-weight: 500; font-size: 15.5px; }
</style>
</head>
<body>
<main class="canvas">
  <section class="card card--front" aria-label="Card front">
    <div class="brand-front">
      <div class="brand-front__square"></div>
      <p class="brand-front__name">Harold Brisk<br>Mechanical</p>
    </div>
    <div class="person">
      <p class="person__name">Daniel Moreau</p>
      <p class="person__role">Managing Director</p>
      <div class="rule"></div>
      <ul class="contact">
        <li><span class="contact__label">P:</span> 052-318 740 615</li>
        <li><span class="contact__label">M:</span> 052-318 740 962</li>
        <li><span class="contact__label">E:</span> desk@hbrisk.com</li>
        <li class="contact__web">www.<span>haroldbrisk</span>.com</li>
      </ul>
      <div class="address-block">
        <div class="rule"></div>
        <p class="address">48 Foundry Lane, Unit 7<br>Eastbridge, EB4 9QT.</p>
      </div>
    </div>
  </section>

  <section class="card card--back" aria-label="Card back">
    <div class="brand-back">
      <div class="brand-back__square"></div>
      <p class="brand-back__name">Harold Brisk Mechanical</p>
    </div>
    <p class="tagline">MECHANICAL &amp; ELECTRICAL CONTRACTORS</p>
    <div class="services">
      <p class="services__title">SPECIALIZING IN SERVICE &amp; INSTALLATION</p>
      <p>Cooling | Heating | Service</p>
      <p>Installations | Residential | Commercial</p>
    </div>
  </section>
</main>
</body>
</html>
```